Ridgeline Outfitters Business Cards

Recently had a logo done with Artfolio and now looking for a business card to go along with it.

Target Market(s)

Ridgeline Outfitters is a weapons dealer. My market will be primarily men, hunting, shooting type.

Industry/Entity Type

Business

Contact Information for Business Card

I selected double sided, but this is not required, single or double is going to be fine. I picture the logo on one side, or perhaps just the circle which contains "RO" with the remaining info on the other side.

Font styles to use
Sans Serif

Requirements
Must have
• My name: Milo Brandt
• Title: Owner
• tel: 612-555-0187
• web: www.ridgelineoutfittersmn.example
Nice to have
• I like the concept of a black business card. I would like to keep the colors monotone, black, grey, white or red. Red is acceptable because it is in the logo. I have also seen cards that are matte black with shiny black as well, perhaps for the logo (or circle RO) part of the logo.
• I will upload a couple of the logos for use, and also an example I just found of the black on black. and some others that have a nice contrast.
Should not have
• lots of colors are not wanted.

```html
<!DOCTYPE html>
<html lang="en">
<head>
<meta charset="utf-8">
<title>Ridgeline Outfitters Business Cards</title>
<link rel="stylesheet" href="https://fonts.googleapis.com/css2?family=Roboto:wght@400;700;900&display=swap">
<style>
  :root {
    --backdrop: #1f1f21;
    --card: #2a2a2c;
    --card-edge: #333335;
    --accent-red: #e3262b;
    --text-light: #e6e6e6;
    --text-muted: #a9a9ab;
    --rule: #8a8a8c;
    --gloss-black: #0d0d0e;
  }
  * { margin: 0; padding: 0; box-sizing: border-box; }
  html, body {
    width: 900px;
    height: 1200px;
    overflow: hidden;
    background: var(--backdrop);
    font-family: "Roboto", Arial, sans-serif;
  }
  .sheet {
    width: 900px;
    height: 1200px;
    display: flex;
    flex-direction: column;
    align-items: center;
    justify-content: space-around;
    padding: 60px 0;
  }
  .card {
    position: relative;
    width: 560px;
    height: 320px;
    background: var(--card);
    border: 1px solid var(--card-edge);
    box-shadow: 0 18px 40px rgba(0,0,0,0.45);
  }
  /* front */
  .brand {
    position: absolute;
    top: 64px;
    left: 44px;
    display: flex;
    align-items: center;
    gap: 16px;
    white-space: nowrap;
  }
  .brand-mark {
    flex: 0 0 64px;
    width: 64px;
    height: 64px;
    border-radius: 50%;
    background: #7a7a7c;
  }
  .brand-name {
    font-weight: 900;
    font-size: 26px;
    letter-spacing: 1px;
    text-transform: uppercase;
    white-space: nowrap;
    color: var(--accent-red);
  }
  .contact {
    position: absolute;
    top: 150px;
    right: 40px;
    text-align: right;
    font-size: 12px;
    line-height: 22px;
    white-space: nowrap;
    color: var(--text-light);
  }
  .divider {
    position: absolute;
    left: 196px;
    right: 40px;
    top: 208px;
    height: 1px;
    background: var(--rule);
  }
  .holder {
    position: absolute;
    left: 44px;
    top: 196px;
    white-space: nowrap;
  }
  .holder-name {
    font-weight: 700;
    font-size: 17px;
    letter-spacing: 0.5px;
    text-transform: uppercase;
    color: var(--text-light);
  }
  .holder-title {
    margin-top: 4px;
    font-size: 11px;
    letter-spacing: 0.5px;
    text-transform: uppercase;
    color: var(--text-muted);
  }
  /* back */
  .card-back .brand {
    top: 0;
    left: 0;
    width: 100%;
    height: 100%;
    justify-content: center;
  }
  .card-back .brand-mark { background: var(--gloss-black); }
  .card-back .brand-name { color: var(--gloss-black); }
</style>
</head>
<body>
<main class="sheet">
  <section class="card card-front">
    <div class="brand">
      <div class="brand-mark"></div>
      <span class="brand-name">Ridgeline Outfitters</span>
    </div>
    <div class="contact">
      <p>P : 612 555 0187</p>
      <p>W : www.ridgelineoutfittersmn.example</p>
    </div>
    <div class="divider"></div>
    <div class="holder">
      <p class="holder-name">Milo Brandt</p>
      <p class="holder-title">Owner</p>
    </div>
  </section>

  <section class="card card-back">
    <div class="brand">
      <div class="brand-mark"></div>
      <span class="brand-name">Ridgeline Outfitters</span>
    </div>
  </section>
</main>
</body>
</html>
```